Harlow Ridge Growers and Nursery needs a business street sign.

I have three businesses located at the same address: The Harlow Ridge Growers & Nursery, The Bramble Nook, and The Quarry Commons. I am looking for a 4’ x 8’ street sign to represent all three businesses as one retail experience. It needs to be eye catching yet simple enough that people can fully read it while driving by. I have logos for the greenhouse and village however I do not have anything for The Bramble Nook. I’m looking for some type of font that’s similar or in between the two attached logos for The Bramble Nook.

• Horizontal Sign, Eye catching, yet simple design so people see it while driving by.
• Horizontal Sign
• I’m open to the design being both vertical and horizontal. Please provide both options

```html
<!DOCTYPE html>
<html lang="en">
<head>
<meta charset="utf-8">
<title>Harlow Ridge Growers &amp; Nursery – Street Sign</title>
<link rel="stylesheet" href="https://fonts.googleapis.com/css2?family=Josefin+Sans:wght@700&display=swap">
<style>
  :root {
    --bg: #f4f4f4;
    --green: #00603a;
    --green-line: rgba(255,255,255,0.35);
    --white: #ffffff;
    --copper: #d19a78;
    --maroon: #8a2b27;
    --font: "Josefin Sans", sans-serif;
  }
  * { box-sizing: border-box; margin: 0; padding: 0; }
  html, body { width: 667px; height: 1200px; overflow: hidden; background: var(--bg); }
  body { position: relative; font-family: var(--font); font-weight: 700; }

  .sign {
    position: absolute;
    background: var(--green);
    box-shadow: 4px 6px 10px rgba(0,0,0,0.18);
    display: flex;
    flex-direction: column;
  }
  .brand-panel {
    background: var(--white);
    border-radius: 5px;
    display: flex;
    align-items: center;
    justify-content: center;
    text-align: center;
    line-height: 1.1;
  }
  .brand-name--growers, .brand-name--nook { color: var(--green); }
  .brand-name--commons { color: var(--maroon); }

  .tagline-box {
    border: 1px solid var(--green-line);
    border-radius: 5px;
    display: flex;
    align-items: center;
    justify-content: center;
    color: var(--white);
  }
  .tagline-arrow { display: block; }
  .rule-label {
    display: flex;
    align-items: center;
    color: var(--copper);
  }
  .rule-label::before, .rule-label::after {
    content: "";
    flex: 1;
    height: 1px;
    background: var(--green-line);
  }
  .headline { color: var(--white); text-align: center; line-height: 1; }

  /* Vertical option */
  .sign--vertical { left: 193px; top: 50px; width: 280px; height: 560px; padding: 7px; gap: 6px; }
  .sign--vertical .brand-panel { height: 131px; flex-shrink: 0; }
  .sign--vertical .brand-name { font-size: 22px; padding: 0 14px; }
  .sign--vertical .tagline-box { height: 58px; flex-direction: column; gap: 6px; font-size: 16px; }
  .sign--vertical .rule-label { font-size: 15px; gap: 8px; margin-top: 2px; }
  .sign--vertical .headline { font-size: 50px; letter-spacing: 10px; padding-left: 10px; }

  /* Horizontal option */
  .sign--horizontal { left: 43px; top: 670px; width: 580px; height: 290px; padding: 7px; gap: 6px; }
  .sign--horizontal .brand-row { display: flex; gap: 6px; height: 136px; }
  .sign--horizontal .brand-panel { flex: 1; }
  .sign--horizontal .brand-name { font-size: 19px; padding: 0 10px; }
  .sign--horizontal .tagline-box { height: 54px; gap: 10px; font-size: 18px; }
  .sign--horizontal .rule-label { font-size: 17px; gap: 10px; margin-top: 2px; }
  .sign--horizontal .headline { font-size: 52px; letter-spacing: 12px; padding-left: 12px; }
</style>
</head>
<body>

  <section class="sign sign--vertical" aria-label="Vertical street sign">
    <div class="brand-panel"><span class="brand-name brand-name--growers">The Harlow Ridge Growers &amp; Nursery</span></div>
    <div class="brand-panel"><span class="brand-name brand-name--commons">Quarry Commons</span></div>
    <div class="brand-panel"><span class="brand-name brand-name--nook">The Bramble Nook</span></div>
    <div class="tagline-box">
      <svg class="tagline-arrow" width="34" height="12" viewBox="0 0 34 12" aria-hidden="true">
        <path d="M1 6H32M26 1L32 6L26 11" fill="none" stroke="var(--copper)" stroke-width="2" stroke-linecap="round" stroke-linejoin="round"/>
      </svg>
      <span>SHOP, BLOOM, EXPLORE</span>
    </div>
    <div class="rule-label">ALL IN ONE</div>
    <div class="headline">PLACE!</div>
  </section>

  <section class="sign sign--horizontal" aria-label="Horizontal street sign">
    <div class="brand-row">
      <div class="brand-panel"><span class="brand-name brand-name--growers">The Harlow Ridge Growers &amp; Nursery</span></div>
      <div class="brand-panel"><span class="brand-name brand-name--commons">Quarry Commons</span></div>
      <div class="brand-panel"><span class="brand-name brand-name--nook">The Bramble Nook</span></div>
    </div>
    <div class="tagline-box">
      <span>SHOP, BLOOM, EXPLORE</span>
      <svg class="tagline-arrow" width="32" height="14" viewBox="0 0 32 14" aria-hidden="true">
        <path d="M1 7H30M24 1L30 7L24 13" fill="none" stroke="var(--copper)" stroke-width="2.2" stroke-linecap="round" stroke-linejoin="round"/>
      </svg>
    </div>
    <div class="rule-label">ALL IN ONE</div>
    <div class="headline">PLACE!</div>
  </section>

</body>
</html>
```